Dental Hygiene referral cards

I am looking to make some referral cards for our hygienists for our dental office. something with our logo and address on the front, and on the back have
hygienist:
__________________
Referred by:
__________________
with a little blurb about what we will give away for a referral.

attached to this is our logo, and a drawing of what im looking for.

I will need this for two of our offices, so just the logo and address will change.

```html
<!DOCTYPE html>
<html lang="en">
<head>
<meta charset="utf-8">
<title>Kestrel Park Dental – Referral Card</title>
<link rel="stylesheet" href="https://fonts.googleapis.com/css2?family=Libre+Baskerville:wght@700&family=Open+Sans:wght@400&display=swap">
<style>
  :root {
    --backdrop: #33b7e7;
    --navy: #1b4580;
    --panel-grey: #eeeeee;
    --band-grey: #999999;
    --white: #ffffff;
  }
  html, body {
    margin: 0;
    width: 1200px;
    height: 1200px;
    overflow: hidden;
    background: var(--backdrop);
  }
  .canvas {
    position: relative;
    width: 1200px;
    height: 1200px;
  }
  .card {
    position: absolute;
    left: 240px;
    width: 676px;
    height: 406px;
    display: block;
  }
  .card--back { top: 67px; }
  .card--front { top: 632px; }
  .serif-heading {
    font-family: "Libre Baskerville", Georgia, serif;
    font-weight: 700;
    fill: var(--navy);
  }
  .field-label { font-size: 26px; }
  .promo-side { font-size: 19px; }
  .promo-blurb { font-size: 16px; }
  .practice-name { font-size: 21px; }
  .brand-name { font-size: 22px; letter-spacing: 0.5px; }
  .contact-text {
    font-family: "Open Sans", Arial, sans-serif;
    font-size: 18px;
    fill: var(--navy);
  }
  .fill-line {
    stroke: var(--navy);
    stroke-width: 2;
  }
  .icon { fill: var(--navy); }
  .icon-stroke { fill: none; stroke: var(--navy); stroke-width: 2; }
</style>
</head>
<body>
<main class="canvas">

  <!-- Referral side -->
  <svg class="card card--back" viewBox="0 0 676 406" xmlns="http://www.w3.org/2000/svg">
    <rect class="card-base" width="676" height="406" fill="var(--white)"/>
    <polygon class="info-panel" points="284,0 676,0 676,375 136,375" fill="var(--panel-grey)"/>
    <polygon class="accent-wedge" points="144,0 284,0 222,158" fill="var(--navy)"/>

    <text class="serif-heading field-label" x="271" y="59">HYGENIST:</text>
    <line class="fill-line" x1="254" y1="110" x2="640" y2="110"/>
    <text class="serif-heading field-label" x="232" y="181">REFERRED BY:</text>
    <line class="fill-line" x1="211" y1="236" x2="640" y2="236"/>

    <text class="serif-heading promo-side">
      <tspan x="30" y="141">FREE</tspan>
      <tspan x="30" y="168">BRIGHTWAVE</tspan>
      <tspan x="30" y="194">TOOTHBRUSH!</tspan>
    </text>

    <text class="serif-heading promo-blurb">
      <tspan x="170" y="311">REFER A PATIENT FOR AN EXAM AND A</tspan>
      <tspan x="170" y="336" textLength="483" lengthAdjust="spacingAndGlyphs">CLEANING AND BOTH OF YOU WILL RECEIVE</tspan>
      <tspan x="170" y="361">A  FREE BRIGHTWAVE TOOTHBRUSH!</tspan>
    </text>

    <rect class="footer-band" x="0" y="375" width="676" height="31" fill="var(--navy)"/>
    <polygon class="footer-gap" points="107,375 306,375 315,406 118,406" fill="var(--white)"/>
    <polygon class="footer-block" points="116,375 296,375 306,406 128,406" fill="var(--band-grey)"/>
  </svg>

  <!-- Practice side -->
  <svg class="card card--front" viewBox="0 0 676 406" xmlns="http://www.w3.org/2000/svg">
    <rect class="card-base" width="676" height="406" fill="var(--white)"/>
    <polygon class="info-panel" points="348,0 676,0 676,374 230,374" fill="var(--panel-grey)"/>
    <polygon class="accent-wedge" points="237,0 348,0 298,157" fill="var(--navy)"/>

    <g class="brand-lockup">
      <circle cx="155" cy="142" r="14" fill="var(--navy)"/>
      <text class="serif-heading brand-name" x="155" y="190" text-anchor="middle">KESTREL PARK</text>
      <text class="serif-heading brand-name" x="155" y="216" text-anchor="middle">DENTAL</text>
    </g>

    <text class="serif-heading practice-name" x="341" y="100">KESTREL PARK DENTAL</text>

    <g class="contact-row">
      <path class="icon" d="M341,135 a11,11 0 0 1 11,11 c0,8 -11,17 -11,17 c0,0 -11,-9 -11,-17 a11,11 0 0 1 11,-11z M341,141 a5,5 0 1 0 0.01,0z" fill-rule="evenodd"/>
      <text class="contact-text" x="376" y="152">123 Street, State, Country</text>
    </g>
    <g class="contact-row">
      <rect class="icon" x="329" y="193" width="24" height="16"/>
      <polyline points="329,194 341,203 353,194" fill="none" stroke="var(--white)" stroke-width="1.8"/>
      <text class="contact-text" x="374" y="208">yourmail@yourwebsite.com</text>
    </g>
    <g class="contact-row">
      <path class="icon" d="M333,236 l5,-2 l4,8 l-3,3 c2,4 5,7 8,9 l3,-3 l8,4 l-2,5 c-12,1 -24,-12 -23,-24z"/>
      <text class="contact-text" x="375" y="254">+00 123 45 67</text>
    </g>
    <g class="contact-row">
      <circle class="icon-stroke" cx="342" cy="301" r="11.5"/>
      <ellipse class="icon-stroke" cx="342" cy="301" rx="5" ry="11.5"/>
      <line class="icon-stroke" x1="330.5" y1="301" x2="353.5" y2="301"/>
      <line class="icon-stroke" x1="332" y1="295" x2="352" y2="295"/>
      <line class="icon-stroke" x1="332" y1="307" x2="352" y2="307"/>
      <text class="contact-text" x="376" y="308">www.yourwebsite.com</text>
    </g>

    <rect class="footer-band" x="0" y="374" width="676" height="32" fill="var(--navy)"/>
    <polygon class="footer-gap" points="91,374 280,374 289,406 102,406" fill="var(--white)"/>
    <polygon class="footer-block" points="100,374 277,374 291,406 111,406" fill="var(--band-grey)"/>
  </svg>

</main>
</body>
</html>
```